2021 Summer Ads Whitmore Ash Custom Homes

We need a re-design of our summer ad run for our customer, Whitmore Ash Custom Homes. They are custom home builders in the mostly rural parts of West Virginia, USA. They are known for their "Forever Home" tagline. We'd like two designed ads with the main difference being just the custom home that's featured. These designs should be for a Google banner like 300 x 250 and square ad like 250 x 250. For inspiration please visit the Whitmore Ash Custom Homes website at www dot whitmoreashcustomhomes dot com

Target Market(s)

consumers / new home shoppers

Industry/Entity Type

Consumer

Requirements
Must have
• WACH logo
Price Lock Available!
Custom home pic
Learn more >
small QVTG logo mark

```html
<!DOCTYPE html>
<html lang="en">
<head>
<meta charset="utf-8">
<title>Whitmore Ash Custom Homes – Summer Ads</title>
<link rel="stylesheet" href="https://fonts.googleapis.com/css2?family=Bebas+Neue&family=Montserrat:wght@500;700;800&family=Allura&display=swap">
<style>
  :root {
    --stage: #5f5e66;
    --red: #d20a11;
    --red-deep: #b1070c;
    --black: #000000;
    --white: #ffffff;
  }
  * { margin: 0; padding: 0; box-sizing: border-box; }
  html, body { width: 1200px; height: 881px; overflow: hidden; }
  body { background: var(--stage); position: relative; font-family: "Montserrat", sans-serif; }

  .ad-slot { position: absolute; width: 573px; height: 477px; overflow: hidden; }
  .ad-slot--first { left: 18px; top: 83px; }
  .ad-slot--second { left: 608px; top: 326px; }

  .ad {
    position: absolute; left: 0; top: 0;
    width: 651px; height: 542px;
    transform: scale(0.8802); transform-origin: 0 0;
    overflow: hidden;
  }
  .ad--red { background: var(--red); }
  .ad--black { background: var(--black); }

  .ad__art { position: absolute; inset: 0; width: 651px; height: 542px; }

  .headline { position: absolute; left: 32px; top: 18px; color: var(--white); }
  .headline__lead { font-weight: 500; font-size: 29px; letter-spacing: 0.5px; line-height: 1.1; }
  .headline__main { font-family: "Bebas Neue", sans-serif; font-size: 62px; line-height: 0.95; letter-spacing: 0.5px; }
  .headline__script {
    position: absolute; left: 300px; top: 96px;
    font-family: "Allura", cursive; font-size: 52px; color: var(--white); white-space: nowrap;
  }

  .brand {
    position: absolute; left: 420px; top: 14px; width: 200px;
    text-align: center; color: var(--red);
    font-weight: 800; font-size: 21px; line-height: 1.1; letter-spacing: 0.5px;
    text-transform: uppercase;
  }

  .price-lock {
    position: absolute; right: 0; width: 200px; height: 84px;
    display: flex; flex-direction: column; justify-content: center; align-items: center;
    color: var(--white); font-weight: 500; font-size: 22px; line-height: 1.25;
  }
  .ad--red .price-lock { left: 451px; top: 259px; background: var(--red-deep); border-top: 3px solid var(--white); border-bottom: 3px solid var(--white); }
  .ad--black .price-lock { left: 425px; top: 266px; width: 226px; background: var(--red); font-weight: 700; border-top: 3px solid var(--white); border-bottom: 3px solid var(--white); }

  .member-badge {
    position: absolute; left: 552px; top: 420px; width: 78px; height: 52px;
    background: var(--white); border-radius: 3px;
  }

  .cta {
    position: absolute; left: 0; top: 480px; width: 651px; height: 62px;
    display: flex; align-items: center;
  }
  .ad--red .cta { background: var(--white); color: var(--red); }
  .ad--black .cta { background: var(--red); color: var(--white); }
  .cta__rule { width: 210px; height: 4px; margin-right: 16px; }
  .ad--red .cta__rule { background: var(--red); }
  .ad--black .cta__rule { background: var(--white); width: 196px; margin-right: 20px; }
  .cta__label { font-weight: 800; font-size: 34px; letter-spacing: 1px; }
  .cta__icon { margin-left: 14px; width: 40px; height: 40px; }
</style>
</head>
<body>

<div class="ad-slot ad-slot--first">
  <div class="ad ad--red">
    <svg class="ad__art" viewBox="0 0 651 542" aria-hidden="false">
      <defs>
        <clipPath id="frame-clip-a"><rect x="0" y="0" width="651" height="480"/></clipPath>
        <linearGradient id="photo-tone-a" x1="0" y1="0" x2="1" y2="1">
          <stop offset="0" stop-color="#9cc6e6"/>
          <stop offset="0.35" stop-color="#6f9a5a"/>
          <stop offset="0.65" stop-color="#e8e9ea"/>
          <stop offset="1" stop-color="#3d5a34"/>
        </linearGradient>
      </defs>
      <circle cx="520" cy="34" r="118" fill="var(--white)"/>
      <g clip-path="url(#frame-clip-a)">
        <ellipse cx="170" cy="480" rx="370" ry="340" fill="var(--white)"/>
        <ellipse cx="170" cy="480" rx="360" ry="330" fill="url(#photo-tone-a)" role="img" aria-label="Photo of a white board-and-batten custom home with a cupola and two garage doors, surrounded by trees and flowering shrubs"/>
      </g>
    </svg>
    <div class="brand">Whitmore Ash<br>Custom Homes</div>
    <div class="headline">
      <p class="headline__lead">Start Building Your</p>
      <p class="headline__main">FOREVER HOME</p>
    </div>
    <p class="headline__script">Today!</p>
    <div class="price-lock"><span>PRICE LOCK</span><span>Available!</span></div>
    <div class="member-badge" role="img" aria-label="Builder association member badge"></div>
    <div class="cta">
      <span class="cta__rule"></span>
      <span class="cta__label">LEARN MORE</span>
      <svg class="cta__icon" viewBox="0 0 40 40" aria-hidden="true">
        <circle cx="20" cy="20" r="19" fill="var(--red)"/>
        <path d="M15 11 L25 20 L15 29" fill="none" stroke="var(--white)" stroke-width="5" stroke-linecap="round" stroke-linejoin="round"/>
      </svg>
    </div>
  </div>
</div>

<div class="ad-slot ad-slot--second">
  <div class="ad ad--black">
    <svg class="ad__art" viewBox="0 0 651 542">
      <defs>
        <clipPath id="frame-clip-b"><rect x="0" y="0" width="651" height="480"/></clipPath>
        <linearGradient id="photo-tone-b" x1="0" y1="0" x2="0" y2="1">
          <stop offset="0" stop-color="#c9dcec"/>
          <stop offset="0.35" stop-color="#4f7a3c"/>
          <stop offset="0.6" stop-color="#a32a26"/>
          <stop offset="0.8" stop-color="#d9d6d0"/>
          <stop offset="1" stop-color="#ecebe6"/>
        </linearGradient>
      </defs>
      <circle cx="520" cy="34" r="122" fill="var(--red)"/>
      <circle cx="520" cy="34" r="116" fill="var(--white)"/>
      <g clip-path="url(#frame-clip-b)">
        <ellipse cx="170" cy="480" rx="372" ry="342" fill="var(--red)"/>
        <ellipse cx="170" cy="480" rx="364" ry="334" fill="var(--white)"/>
        <ellipse cx="170" cy="480" rx="358" ry="328" fill="url(#photo-tone-b)" role="img" aria-label="Photo of a finished white ranch home with a red barn-style garage, set against a line of green trees"/>
      </g>
    </svg>
    <div class="brand">Whitmore Ash<br>Custom Homes</div>
    <div class="headline">
      <p class="headline__lead">Start Building Your</p>
      <p class="headline__main">FOREVER HOME</p>
    </div>
    <p class="headline__script">Today!</p>
    <div class="price-lock"><span>PRICE LOCK</span><span>Available!</span></div>
    <div class="member-badge" role="img" aria-label="Builder association member badge"></div>
    <div class="cta">
      <span class="cta__rule"></span>
      <span class="cta__label">LEARN MORE</span>
      <svg class="cta__icon" viewBox="0 0 40 40" aria-hidden="true">
        <circle cx="20" cy="20" r="19" fill="var(--white)"/>
        <path d="M15 11 L25 20 L15 29" fill="none" stroke="var(--red)" stroke-width="5" stroke-linecap="round" stroke-linejoin="round"/>
      </svg>
    </div>
  </div>
</div>

</body>
</html>
```